Veltrona Web Presence

I need a word press site for my company that houses diverse services, and am looking to profile these areas: Design and Delivery of Social Innovation Initiatives, Innovative Pubic Engagement, The Turquoise Economy, Youth Entrepreneurship, and The Science of Change.

I would also like to profile my recent projects. A blog, video and photos are also important features.

Industry/Entity Type

It Company

Requirements
Must have
• I would like to have an overview of what the company does as a Think, Feel and Do Company, along with sections for specific services and recent project profiles.

I would like a section for a blog

I would like a section for photos and video.

I would like the look and feel of the website to reflect the following:

Marisol has spent 30 years leading expeditions into the future. Marisol has a special interest in exploring the changing business, social and cultural landscapes and frontiers, uncovering uncharted territory and unleashing hidden potential – within the person, family, organization, community, business or marketplace. Marisol thrives on experimentation that has led to blended eastern and western methodologies and technologies that help people and organizations deal with the chronic and tough issues in research-based, intelligent and inspiring ways.

Specialties:Breaking down the walls between disciplines such as environmental, social, and economic approaches to create ideologies and methodologies that weave them all to change the way we live. This ideology and methodology applies to all areas: business development, business identity, strategy for all organizations - public, private and NGO.This starts at the individual level.Marisol is also an energy healer specializing in belief reconstruction leading to fulfilling lives.

```html
<!DOCTYPE html>
<html lang="en">
<head>
<meta charset="utf-8">
<title>Veltrona</title>
<link href="https://fonts.googleapis.com/css2?family=Bebas+Neue&family=Open+Sans:wght@300;400;600;700&display=swap" rel="stylesheet">
<style>
:root{
  --blue:#0b62b5;
  --blue-dark:#0754a0;
  --blue-light:#2aa8e0;
  --orange:#fbad1a;
  --ink:#7b7f86;
  --title:#0b62b5;
  --bg:#f3f5f8;
  --black:#050505;
  --white:#ffffff;
}
*{box-sizing:border-box;margin:0;padding:0}
html,body{width:973px;height:1200px;overflow:hidden}
body{background:var(--bg);font-family:"Open Sans",sans-serif;color:var(--ink);position:relative}
.wrap{position:absolute;left:163px;width:648px}

/* header */
.site-header{position:absolute;top:0;left:0;width:973px;height:62px;background:var(--white)}
.brand{position:absolute;left:164px;top:12px;display:flex;align-items:center;gap:8px}
.brand-dot{width:14px;height:14px;border-radius:50%;background:var(--blue-light)}
.brand-name{font-family:"Open Sans",sans-serif;font-weight:300;font-size:30px;color:var(--blue-light);letter-spacing:.5px}
.social-top{position:absolute;top:20px;left:675px;display:flex;gap:3px}
.social-top span{width:25px;height:25px;border-radius:50%;display:block}
.s1{background:#3aa3dc}.s2{background:#2f5597}.s3{background:#333}.s4{background:#7ed0ea}.s5{background:#1ea6e6}

.main-nav{position:absolute;top:62px;left:0;width:973px;height:42px;background:var(--blue);border-bottom:4px solid var(--blue-light)}
.main-nav ul{position:absolute;left:165px;top:14px;display:flex;list-style:none}
.main-nav li{font-size:9px;font-weight:700;color:var(--white);padding:0 14px;border-left:1px solid rgba(255,255,255,.25);line-height:11px}
.main-nav li:first-child{padding-left:0;border-left:none}
.search{position:absolute;left:656px;top:10px;display:flex;height:20px}
.search-input{width:115px;background:var(--white);font-size:5.5px;color:#aaa;padding:7px 10px}
.search-btn{width:40px;background:var(--orange);color:var(--white);font-size:6px;text-align:center;line-height:20px}

/* hero */
.hero{position:absolute;top:104px;left:0;width:973px;height:384px;background:linear-gradient(100deg,#c9d3dc 0%,#e4e9ee 40%,#aab4bd 62%,#2c2a2c 70%,#d8dde2 85%,#c2ccd4 100%)}
.hero-box{position:absolute;left:163px;top:79px;width:309px;height:189px;background:rgba(11,98,181,.9);padding:10px 14px;color:var(--white)}
.hero-kicker{font-family:"Bebas Neue",sans-serif;font-size:28px;line-height:28px}
.hero-title{font-family:"Bebas Neue",sans-serif;font-size:62px;line-height:56px}
.hero-text{font-size:10.5px;font-weight:300;line-height:12.5px;margin-top:4px}
.btn{display:inline-block;background:var(--orange);color:var(--white);font-weight:700;font-size:9.5px;padding:6px 10px}
.hero-box .btn{margin-top:6px}
.welcome{position:absolute;left:0;top:332px;width:540px;height:52px;background:var(--orange);clip-path:polygon(0 0,475px 0,540px 52px,0 52px)}
.welcome h2{position:absolute;left:163px;top:4px;font-family:"Bebas Neue",sans-serif;font-weight:400;font-size:44px;color:var(--white);letter-spacing:-1px}
.hero-rule{position:absolute;left:0;top:380px;width:973px;height:4px;background:var(--orange)}
.pager{position:absolute;display:flex;gap:2px}
.pager span{width:24px;height:24px;background:var(--blue);display:flex;align-items:center;justify-content:center}
.hero .pager{left:761px;top:356px}

/* intro */
.section-title{font-family:"Bebas Neue",sans-serif;font-weight:400;font-size:34px;line-height:30px;color:var(--title);display:inline-block;border-bottom:1px dotted var(--title);padding-bottom:2px;letter-spacing:-1px}
.intro{top:505px}
.intro-text{width:360px;font-size:9px;font-weight:300;line-height:12.8px;margin-top:8px;color:#8b8f95}
.intro .btn{margin-top:10px}
.video{position:absolute;left:553px;top:510px;width:258px;height:200px;background:#e8eaec;border:1px solid #cfd3d6;box-shadow:0 2px 4px rgba(0,0,0,.15)}
.video-bar{height:10px;font-size:4px;color:#666;padding:3px 6px}
.video-screen{margin:0 2px;height:162px;background:linear-gradient(#202224 0 48%,#000 48%);display:flex;align-items:center;justify-content:center}
.video-screen span{font-weight:300;font-size:26px;color:var(--blue-light)}
.video-controls{height:26px;display:flex;align-items:center;padding:0 6px;gap:6px}
.video-time{font-size:4.5px;color:#666;background:#fff;border:1px solid #ccc;padding:1px 3px}
.ctrl{width:7px;height:7px;border-radius:50%;background:#c8ccc9}
.ctrl.play{background:#8fbf4a}
.vol{margin-left:auto;width:36px;height:5px;background:linear-gradient(90deg,#7fbf3a 50%,#ddd 50%)}

/* services */
.services{position:absolute;top:727px;left:0;width:973px;height:149px;background:linear-gradient(#1670c7,#0b5eae);box-shadow:0 3px 6px rgba(0,0,0,.15)}
.services .section-title{position:absolute;left:163px;top:10px;color:var(--white);border-color:var(--white)}
.service{position:absolute;top:48px;width:140px;text-align:center;color:var(--white);font-size:11.5px;line-height:14px;letter-spacing:-.5px}
.service svg{display:block;margin:0 auto 12px}

/* projects */
.projects{top:898px}
.projects .pager{left:611px;top:20px}
.project-img{position:absolute;top:45px;width:209px;height:114px}
.p1{left:0;background:linear-gradient(135deg,#5b5f66,#d8dadc 50%,#6d7075)}
.p2{left:219px;background:linear-gradient(135deg,#f1f2f3,#cfd6de 50%,#5a8cc7)}
.p3{left:440px;background:linear-gradient(135deg,#ececec,#d9dbdc 50%,#b4b6b8)}

/* footer */
.site-footer{position:absolute;top:1076px;left:0;width:973px;height:124px;background:var(--black);border-top:4px solid var(--blue);color:var(--white)}
.footer-title{font-size:11.5px;font-weight:700;letter-spacing:-.5px;display:inline-block;border-bottom:1px dotted #888;padding-bottom:1px}
.footer-about{position:absolute;left:164px;top:12px;width:380px}
.footer-about p{font-size:7px;line-height:9.2px;margin-top:6px;color:#ddd}
.footer-about .more{font-size:7px;font-weight:700;margin-top:4px}
.footer-links{position:absolute;left:164px;top:98px;font-size:8px}
.footer-contact{position:absolute;left:581px;top:12px;font-size:7px;line-height:11px}
.footer-contact p:first-of-type{margin-top:6px}
.footer-contact .strong{font-weight:700}
.footer-connect{position:absolute;left:714px;top:12px;width:98px}
.footer-icons{display:flex;gap:4px;margin:8px 0 0 11px}
.footer-icons span{width:20px;height:20px;border-radius:50%;background:var(--white);border:2px solid var(--blue)}
.footer-brand{margin:12px 0 0 8px;display:flex;align-items:center;gap:5px}
.footer-brand .dot{width:9px;height:9px;border-radius:50%;background:#bbb}
.footer-brand span:last-child{font-weight:300;font-size:19px;color:#ddd}
</style>
</head>
<body>

<header class="site-header">
  <div class="brand"><span class="brand-dot"></span><span class="brand-name">Veltrona</span></div>
  <div class="social-top" aria-label="Social links"><span class="s1"></span><span class="s2"></span><span class="s3"></span><span class="s4"></span><span class="s5"></span></div>
</header>

<nav class="main-nav">
  <ul><li>HOME</li><li>WHO WE ARE</li><li>WHAT WE DO</li><li>BLOG</li><li>PROJECTS</li><li>CONTACT US</li></ul>
  <div class="search"><div class="search-input">SEARCH HERE.....</div><div class="search-btn">SEARCH</div></div>
</nav>

<section class="hero" role="img" aria-label="Businesswoman in a dark suit standing arms crossed before office windows overlooking a city">
  <div class="hero-box">
    <div class="hero-kicker">LOREM</div>
    <div class="hero-title">VELTRONA</div>
    <p class="hero-text">Lorem ipsum dolor sit amet, consectetuer adipiscing elit, sed diam nonummy nibh euismod tincidunt ut laoreet dolore magna aliquam erat volutpat. Ut wisi enim ad minim veniam, quis.</p>
    <span class="btn">READ MORE</span>
  </div>
  <div class="welcome"><h2>Welcome to VELTRONA</h2></div>
  <div class="hero-rule"></div>
  <div class="pager">
    <span><svg width="10" height="14" viewBox="0 0 10 14"><path d="M8 1 2 7l6 6" stroke="#fff" stroke-width="2.5" fill="none"/></svg></span>
    <span><svg width="10" height="14" viewBox="0 0 10 14"><path d="m2 1 6 6-6 6" stroke="#fff" stroke-width="2.5" fill="none"/></svg></span>
  </div>
</section>

<section class="wrap intro">
  <h2 class="section-title">INTRODUCTION.</h2>
  <p class="intro-text">Marisol has spent 30 years leading expeditions into the future. Marisol has a special interest in exploring the changing business, social and cultural landscapes and frontiers, uncovering uncharted territory and unleashing hidden potential – within the person, family, organization, community, business or marketplace. Marisol thrives on experimentation that has led to blended eastern and western methodologies and technologies that help people and organizations deal with the chronic and tough issues in research-based, intelligent and inspiring waysBreaking down the walls between disciplines such as environmental, social, and economic approaches to create ideologies and methodologies that weave them all to change the way we live. This ideology and methodology applies to all areas: business development, business identity, strategy.</p>
  <span class="btn">READ MORE</span>
</section>

<div class="video">
  <div class="video-bar">Menu</div>
  <div class="video-screen"><span>Veltrona</span></div>
  <div class="video-controls">
    <span class="video-time">00:00</span>
    <span style="margin-left:40px" class="ctrl"></span><span class="ctrl"></span><span class="ctrl play"></span><span class="ctrl"></span><span class="ctrl"></span>
    <span class="vol"></span>
  </div>
</div>

<section class="services">
  <h2 class="section-title">OUR SERVICES.</h2>
  <div class="service" style="left:140px">
    <svg width="48" height="48" viewBox="0 0 48 48" fill="none" stroke="#fff" stroke-width="6"><path d="M4 12h10l20 24h8M4 36h10l20-24h8"/><path d="M38 4l8 8-8 8M38 28l8 8-8 8" stroke-width="4" fill="#fff"/></svg>
    INNOVATIVE PUBIC<br>ENGAGEMENT</div>
  <div class="service" style="left:280px">
    <svg width="48" height="48" viewBox="0 0 48 48" fill="#fff"><circle cx="24" cy="21" r="10"/><rect x="19" y="31" width="10" height="8" rx="2"/><path d="M24 2v5M8 10l4 4M40 10l-4 4M3 23h5M40 23h5M10 38l4-4M38 38l-4-4" stroke="#fff" stroke-width="3"/></svg>
    SOCIAL INNOVATION<br>INITIATIVES</div>
  <div class="service" style="left:428px">
    <svg width="48" height="48" viewBox="0 0 48 48" fill="#fff"><circle cx="17" cy="14" r="8"/><circle cx="33" cy="14" r="8"/><path d="M2 40c0-10 7-16 15-16s15 6 15 16zM20 40c0-10 6-16 13-16s13 6 13 16z"/></svg>
    YOUTH<br>ENTREPRENEURSHIP</div>
  <div class="service" style="left:570px">
    <svg width="48" height="48" viewBox="0 0 48 48" fill="#fff"><path d="M22 6a20 20 0 1 0 20 20H22z"/><path d="M26 2a20 20 0 0 1 20 20H26z" fill="none" stroke="#fff" stroke-width="3"/></svg>
    THE TURQUOISE<br>ECONOMY</div>
  <div class="service" style="left:700px">
    <svg width="48" height="48" viewBox="0 0 48 48" fill="none" stroke="#fff" stroke-width="4"><circle cx="24" cy="26" r="19"/><circle cx="24" cy="26" r="9"/><path d="M24 26 36 14"/></svg>
    THE SCIENCE OF<br>CHANGE.</div>
</section>

<section class="wrap projects">
  <h2 class="section-title">RECENT PROJECTS.</h2>
  <div class="pager">
    <span style="width:18px;height:18px"><svg width="8" height="12" viewBox="0 0 10 14"><path d="M8 1 2 7l6 6" stroke="#fff" stroke-width="2.5" fill="none"/></svg></span>
    <span style="width:18px;height:18px"><svg width="8" height="12" viewBox="0 0 10 14"><path d="m2 1 6 6-6 6" stroke="#fff" stroke-width="2.5" fill="none"/></svg></span>
  </div>
  <div class="project-img p1" role="img" aria-label="Open hands holding a network of glowing people icons before business figures"></div>
  <div class="project-img p2" role="img" aria-label="Hands with pens reviewing printed blue bar charts"></div>
  <div class="project-img p3" role="img" aria-label="Hands sketching a plan on paper during a meeting"></div>
</section>

<footer class="site-footer">
  <div class="footer-about">
    <h3 class="footer-title">ABOUT US</h3>
    <p>Lorem ipsum dolor sit amet, consectetuer adipiscing elit, sed diam nonummy nibh euismod tincidunt ut laoreet dolore magna aliquam erat volutpat. Ut wisi enim ad minim veniam, quis nostrud exerci tation ullamcorper suscipit lobortis nisl ut aliquip ex ea commodo consequat. Duis autem vel eum iriure dolor in hendrerit.</p>
    <p class="more">READ MORE</p>
  </div>
  <div class="footer-links">ABOUT US | CONTACT US | FAQ | PRIVACY POLICY | TERMS &amp; CONDITIONS</div>
  <div class="footer-contact">
    <h3 class="footer-title">CONTACT US</h3>
    <p class="strong">LINDENWEG 14</p>
    <p class="strong">A 4410 MARBACH</p>
    <p>+ 43 (0) 5512 / 40870-0</p>
    <p>+ 43 (0) 5512 / 40870-150</p>
  </div>
  <div class="footer-connect">
    <h3 class="footer-title">CONNECT WITH US</h3>
    <div class="footer-icons"><span></span><span></span><span></span></div>
    <div class="footer-brand"><span class="dot"></span><span>Veltrona</span></div>
  </div>
</footer>

</body>
</html>
```